Banner for homepage

It is a new banner for the homepage, temporary site address is 61.187.40.72 ( is the biggest banner only ) . Would be 5 variations for image content as below (in Portuguese ) :

Image 1:
Leitor de codigo de barras
Todos os tipos de leitores de código de barras para as mais diversas aplicações.
( example of product images in : http://www.quentorlabs.com/en-US/Pages/Category.aspx?category=barcode-scanners&cat=KLT)

Image 2:
Impressora de etiquetas
Identifique o que for nessário com o melhor custo/beneficio e flexibilidade de materiais de impressão.
( example of product images in : vintor.com in label printers desktop and industrial)

Image 3:
Impressora de cupom
Imprima recibos e cupons fiscais com agilidade e qualidade, temos a impressora certa para o seu PDV.
( example of product images in : http://www.palutrek.com.br/equipamento-categoria-impressoras+fiscais.html)

Image 4:
Coletor de dados
Computadores móveis com leitor de código de barras, que levam a automação para frente de trabalho.
( example of product images in : http://www.quentorlabs.com/en-US/Pages/Category.aspx?cat=KLT&category=hand-held-mobile-computer)

Image 5:
Etiquetas e Ribbons:
Etiquetas adesivas e não adesivas em vários de tipos de materiais, papéis e plásticos. O ribbon certo para impressão perfeita em cada material.
( example of product images in : http://www.tagmirelo.com/cats/supplies/barcode-printer.htm?nav=hdr)

```html
<!DOCTYPE html>
<html lang="pt-BR">
<head>
<meta charset="utf-8">
<title>Etiquetas e Ribbons</title>
<link href="https://fonts.googleapis.com/css2?family=Arimo:wght@400;700&display=swap" rel="stylesheet">
<style>
  :root {
    --bg-light: #f4f4f4;
    --bg-mid: #d6d6d6;
    --bg-dark: #9a9a9a;
    --title-top: #ff9a2e;
    --title-bottom: #e0260c;
    --body-text: #151515;
    --button-top: #e8412f;
    --button-bottom: #8e0d07;
    --button-text: #ffffff;
    --product-light: #e9ecef;
    --product-dark: #3a4a7a;
  }
  html, body {
    margin: 0;
    padding: 0;
    width: 1200px;
    height: 549px;
    overflow: hidden;
    background: var(--bg-mid);
  }
  .banner {
    position: relative;
    width: 1200px;
    height: 549px;
    overflow: hidden;
    font-family: "Arimo", Arial, sans-serif;
    background:
      radial-gradient(ellipse 420px 300px at 1030px 40px, rgba(255,255,255,0.95), rgba(255,255,255,0) 70%),
      radial-gradient(ellipse 700px 380px at 380px 260px, var(--bg-light), rgba(244,244,244,0) 80%),
      linear-gradient(180deg, #c9c9c9 0%, #e2e2e2 45%, #bdbdbd 80%, var(--bg-dark) 100%);
  }
  .banner__title {
    position: absolute;
    left: 38px;
    top: 92px;
    margin: 0;
    font-size: 64px;
    font-weight: 700;
    letter-spacing: -0.5px;
    line-height: 1;
    background: linear-gradient(180deg, var(--title-top) 10%, var(--title-bottom) 90%);
    -webkit-background-clip: text;
    background-clip: text;
    color: transparent;
    filter: drop-shadow(0 0 6px rgba(255,255,255,0.9));
  }
  .banner__text {
    position: absolute;
    left: 38px;
    top: 186px;
    width: 820px;
    margin: 0;
    font-size: 29px;
    line-height: 37px;
    color: var(--body-text);
  }
  .banner__button {
    position: absolute;
    left: 65px;
    top: 442px;
    width: 224px;
    height: 62px;
    border-radius: 31px;
    background: linear-gradient(180deg, var(--button-top) 0%, #c51e12 50%, var(--button-bottom) 100%);
    box-shadow: 0 4px 8px rgba(0,0,0,0.35), inset 0 2px 2px rgba(255,255,255,0.35);
    display: flex;
    align-items: center;
    text-decoration: none;
    color: var(--button-text);
    font-size: 27px;
  }
  .banner__button-icon {
    width: 44px;
    height: 44px;
    margin: 0 16px 0 9px;
  }
  .banner__products {
    position: absolute;
    left: 608px;
    top: 291px;
    width: 575px;
    height: 240px;
    border-radius: 10px;
    background: linear-gradient(100deg, var(--product-light) 0%, #d9dde2 50%, #6a7390 78%, var(--product-dark) 100%);
  }
</style>
</head>
<body>
  <section class="banner">
    <h1 class="banner__title">Etiquetas e Ribbons</h1>
    <p class="banner__text">Etiquetas adesivas e não adesivas em vários de tipos de materiais, papéis e plásticos. O ribbon certo para impressão perfeita em cada material.</p>
    <a class="banner__button" href="#">
      <svg class="banner__button-icon" viewBox="0 0 44 44" aria-hidden="true">
        <circle cx="22" cy="22" r="20" fill="#7a0a05" stroke="#ffffff" stroke-width="3"/>
        <path d="M17 13 L31 22 L17 31 Z" fill="#ffffff"/>
      </svg>
      Veja Mais
    </a>
    <div class="banner__products" role="img" aria-label="Rolos de etiquetas brancas e rolos de ribbon pretos e azuis"></div>
  </section>
</body>
</html>
```